Word document template for sales proposals

I am after a template that is simple but impactful. Use of colour to be limited but some for impact would be good. The proposals are for use in the professional technical field.

```html
<!DOCTYPE html>
<html lang="en">
<head>
<meta charset="utf-8">
<title>Pricing &amp; Terms – Sales Proposal</title>
<link href="https://fonts.googleapis.com/css2?family=Carlito:wght@400;700&display=swap" rel="stylesheet">
<style>
  :root {
    --brand-blue: #29a9e0;
    --brand-orange: #f7941d;
    --ink: #111111;
    --paper: #ffffff;
  }
  html, body {
    margin: 0;
    padding: 0;
    overflow: hidden;
    background: var(--paper);
  }
  .page {
    position: relative;
    width: 849px;
    height: 1200px;
    overflow: hidden;
    background: var(--paper);
    font-family: "Carlito", "Calibri", sans-serif;
    color: var(--ink);
  }
  .header-band {
    position: absolute;
    left: 0;
    top: 111px;
    width: 618px;
    height: 22px;
    background: var(--brand-blue);
  }
  .brand {
    position: absolute;
    left: 627px;
    top: 95px;
    display: flex;
    align-items: center;
    gap: 8px;
  }
  .brand-mark {
    width: 44px;
    height: 44px;
    border-radius: 50%;
    background: var(--brand-blue);
  }
  .brand-name {
    font-size: 32px;
    font-weight: 400;
    color: var(--brand-orange);
    letter-spacing: 0.5px;
  }
  .section-title {
    position: absolute;
    left: 100px;
    margin: 0;
    font-size: 36px;
    font-weight: 400;
    line-height: 44px;
    letter-spacing: -0.2px;
  }
  .item-title {
    position: absolute;
    left: 100px;
    margin: 0;
    font-size: 18.5px;
    font-weight: 400;
    line-height: 24px;
  }
  .item-text {
    position: absolute;
    left: 100px;
    width: 660px;
    margin: 0;
    font-size: 13.9px;
    line-height: 21.4px;
    letter-spacing: 0.3px;
  }
</style>
</head>
<body>
<main class="page">
  <div class="header-band"></div>
  <div class="brand">
    <div class="brand-mark"></div>
    <span class="brand-name">Norvale</span>
  </div>

  <h1 class="section-title" style="top:180px">Pricing &amp; Terms</h1>
  <h2 class="item-title" style="top:241px">Price</h2>
  <p class="item-text" style="top:267px">Provide pricing details and purchasing options.&nbsp; Be sure to include any additional expenses such as travel for professional services staff.</p>
  <h2 class="item-title" style="top:329px">Terms</h2>
  <p class="item-text" style="top:355px">State the terms and conditions for the deal.</p>

  <h1 class="section-title" style="top:391px">Contact Information</h1>
  <h2 class="item-title" style="top:454px">Headquarters</h2>
  <p class="item-text" style="top:479px">Provide the address and contact information for your headquarters.</p>
  <h2 class="item-title" style="top:520px">Account Manager</h2>
  <p class="item-text" style="top:545px">Provide the contact information for the Account Manager</p>
  <h2 class="item-title" style="top:586px">VP Sales</h2>
  <p class="item-text" style="top:611px">Provide the contact information for the VP Sales.</p>

  <h1 class="section-title" style="top:648px">Appendix</h1>
  <h2 class="item-title" style="top:710px">Additional Information</h2>
  <p class="item-text" style="top:737px">Provide any additional information such as a service level agreement, satisfaction guarantee, customer references, testimonials etc.</p>
</main>
</body>
</html>
```